Modern Business Card Design
Consulting firm - Engineering/Infrastructure Sector
Use same font as used in my logo
but we are open to new fonts, as long as the printer will not have trouble with them.
Professional
Melanie Trovaskis
Partner
4215 Linwood Avenue
Suite 207
mtrovaskis@brightholmpx.com
www.brightholmpx.com
we're looking for something sharp and complementary to our logo

```html
<!DOCTYPE html>
<html lang="en">
<head>
<meta charset="utf-8">
<title>Brightholm Business Cards</title>
<link rel="stylesheet" href="https://fonts.googleapis.com/css2?family=Cormorant+Garamond:wght@500&display=swap">
<style>
  :root {
    --bg: #e4e6ea;
    --card: #ffffff;
    --navy: #1b3a8c;
    --sky: #3f9be0;
    --pale: #b9dcf4;
    --ink: #2a3450;
    --shadow: rgba(20, 30, 60, 0.18);
  }
  * { margin: 0; padding: 0; box-sizing: border-box; }
  html, body {
    width: 1200px; height: 1005px; overflow: hidden;
    background: var(--bg);
    font-family: "Cormorant Garamond", Georgia, serif;
    font-weight: 500;
  }
  .card {
    position: absolute; left: 197px;
    width: 805px; height: 460px;
    background: var(--card);
    border-radius: 22px;
    box-shadow: 0 10px 30px var(--shadow);
    overflow: hidden;
  }
  .card--front { top: 28px; }
  .card--back { top: 517px; }

  .brand-name {
    position: absolute;
    color: var(--navy);
    font-weight: 500;
    letter-spacing: 3px;
    text-transform: uppercase;
    line-height: 1;
  }
  .card--front .brand-name { left: 250px; top: 72px; font-size: 54px; }

  .person { position: absolute; left: 48px; top: 178px; width: 340px; text-align: right; }
  .person__name {
    color: var(--sky); font-size: 30px; font-weight: 500;
    text-align: left; margin-bottom: 6px; letter-spacing: 1px;
  }
  .person__line { color: var(--ink); font-size: 18px; line-height: 25px; letter-spacing: 1px; }

  .divider { position: absolute; left: 402px; top: 222px; width: 1px; height: 112px; background: var(--ink); }

  .contacts { position: absolute; left: 418px; top: 218px; list-style: none; }
  .contacts li {
    display: flex; align-items: center; gap: 9px;
    color: var(--ink); font-size: 17px; line-height: 23px; letter-spacing: 0.5px;
  }
  .contacts svg { width: 11px; height: 11px; flex: none; }

  .footer-band {
    position: absolute; left: 0; bottom: 0;
    width: 805px; height: 90px;
    background: linear-gradient(180deg, var(--pale) 0%, var(--sky) 45%, var(--navy) 100%);
  }

  .card--back .brand-name { left: 0; width: 805px; top: 170px; font-size: 60px; text-align: center; }
  .website {
    position: absolute; left: 0; width: 805px; top: 262px; text-align: center;
    color: var(--ink); font-size: 24px; letter-spacing: 4px; text-transform: uppercase;
  }
</style>
</head>
<body>

<section class="card card--front" aria-label="Business card front">
  <p class="brand-name">Brightholm</p>

  <div class="person">
    <h1 class="person__name">Melanie Trovaskis</h1>
    <p class="person__line">Partner</p>
    <p class="person__line">4215 Linwood Avenue</p>
    <p class="person__line">Suite 207</p>
  </div>

  <div class="divider"></div>

  <ul class="contacts">
    <li><svg viewBox="0 0 12 12" aria-hidden="true"><circle cx="6" cy="6" r="6" fill="var(--navy)"/></svg>410-555-0182</li>
    <li><svg viewBox="0 0 12 12" aria-hidden="true"><circle cx="6" cy="6" r="6" fill="var(--navy)"/></svg>410-555-0197</li>
    <li><svg viewBox="0 0 12 12" aria-hidden="true"><circle cx="6" cy="6" r="6" fill="var(--navy)"/></svg>443-555-0126</li>
    <li><svg viewBox="0 0 12 12" aria-hidden="true"><circle cx="6" cy="6" r="6" fill="var(--navy)"/></svg>mtrovaskis@brightholmpx.com</li>
    <li><svg viewBox="0 0 12 12" aria-hidden="true"><circle cx="6" cy="6" r="6" fill="var(--navy)"/></svg>www.brightholmpx.com</li>
  </ul>

  <div class="footer-band" role="img" aria-label="Decorative blue band along the bottom edge"></div>
</section>

<section class="card card--back" aria-label="Business card back">
  <p class="brand-name">Brightholm</p>
  <p class="website">www.brightholmpx.com</p>
</section>

</body>
</html>
```